website for shopify- Almond Steward. Natural Peanut Butter Mixer

I need a website for shopify for my invention...The AlmondSteward. ( Registered trademark)
They are kitchen accessories for mixing Natural peanut butter (9 mixing hooks). Natural peanut butter separates with oil floating to the top when it sits on the shelf. Very hard and messy to mix it in manually.

My hook is compatible with 8 popular brand name electric hand mixers, plus 1/4” HEX universal drill bit. (9 total)

The mixing Hook part that goes into the nut butter is all the same for each hook, it’s just locking interface changes for each hook. I will supply a close up photo for each hook lock mechanism. ( leave blank until Thursday next week)
Brands are: Gray and Fenwick, Vellomix, Corwin Harbor, StoveMate, Brelda, Halvern Trope, Glowline Modern, Glowline Retro.
Plus 1/4” HEX quick lock drill bit.

I would like to inspire with complementary healthy peanut butter snack images..as peanut butter is pretty brown!!
There are lots of beautiful stock photos of peanut butter snacks on framevault or Picbarn. Samples included in my files. My logo needs to have Registered trade Mark R in circle ⭕️ added to end of logo.
Plus I would like a couple of smiling moms with kids eating peanut butter.

Target Market(s)

North American health food minded people.

Coding

Number of Pages Required

5+ page

Font styles to use
Sans Serif

Colors
ffffff
ec1f27
f78f20
9bcb3c

Requirements
Must have
• I have about 6 sections in my 1 page website to design....page 7 thru 15 are all the same with just photo and brand name changes and list of model numbers compatible, for each different mixing hook.

I want my headline to rotate with 3 changing words.
Natural Peanut Butter
1) Mixed Perfectly 2) Better Tasting 3) Hassle-Free

Want to add shop now button on all pages.

Clean white background. I like shadow colour boxes behind clusters of 2-3 photos. Contemporary look.
I can type and upload blog pages soon so you don’t have to type them in. Just add a few photos.
Patented Design!!! Important to add so copy cats don’t copy.
Nice to have
• Complementary 3 colour palette that doesn’t change. Red being one.
Open to seeing other colour palettes.
Should not have
• Logos of any brand names. Just written in a clear black font consistent for all.

```html
<!DOCTYPE html>
<html lang="en">
<head>
<meta charset="utf-8">
<title>Almond Steward — Natural Peanut Butter Mixer</title>
<link href="https://fonts.googleapis.com/css2?family=Audiowide&family=Roboto:ital,wght@0,400;0,500;0,700;1,400;1,500;1,700&display=swap" rel="stylesheet">
<style>
:root{
  --cream:#ede3d5;
  --brown:#8c5a4e;
  --tan:#d9c0a5;
  --paper:#faf6f1;
  --clay:#d18f77;
  --ink:#1a1a1a;
  --white:#ffffff;
  --footer:#111111;
  --muted:#c9c9c9;
  --star:#f0b400;
  --gold:#f5b321;
  --red:#e0341f;
  --orange:#f78f20;
}
*{box-sizing:border-box;margin:0;padding:0}
html,body{width:1200px;height:4532px;overflow:hidden}
body{position:relative;font-family:'Roboto',sans-serif;color:var(--ink);background:var(--white)}
.abs{position:absolute}
.display{font-family:'Audiowide',sans-serif;font-weight:400}
.center{text-align:center}
.btn{position:absolute;background:var(--brown);color:var(--white);font-size:16px;font-weight:500;display:flex;align-items:center;justify-content:center;gap:8px}
.btn svg{width:16px;height:16px}

/* hero */
.hero{position:absolute;left:0;top:0;width:1200px;height:646px;background:var(--cream)}
.brand-top{left:100px;top:44px;font-size:20px;font-weight:500;color:var(--brown);letter-spacing:1px}
.nav{right:100px;top:28px;font-size:14px;font-weight:500;display:flex;gap:14px}
.hero-title{left:0;width:1200px;top:118px;font-size:40px;letter-spacing:2px}
.hero-sub{left:0;width:1200px;top:172px;font-size:27px}
.feature-label{font-size:23px;font-weight:500}
.bowl{left:385px;top:305px;width:428px;height:428px;border-radius:50%;
  background:radial-gradient(circle at 48% 45%,#e6b070 0,#d89a4e 30%,#c98a42 50%,#b8763a 60%,#f6f3ee 62.5%,#e4ded6 100%);
  box-shadow:0 8px 22px rgba(0,0,0,.18);z-index:3}

/* how it works */
.how{position:absolute;left:0;top:646px;width:1200px;height:527px;background:var(--brown)}
.how-photo{left:0;top:0;width:440px;height:527px;background:linear-gradient(100deg,#c9574f 0,#b8605a 45%,rgba(140,90,78,0) 100%)}
.how-title{left:500px;top:108px;font-size:40px;color:var(--white);letter-spacing:2px}
.step{position:absolute;width:275px;color:var(--white);font-size:18px;line-height:1.4}
.step svg{display:block;width:52px;height:56px;margin-bottom:16px}

/* price */
.price{position:absolute;left:0;top:1173px;width:1200px;height:375px;background:var(--tan)}
.bump{left:475px;top:1098px;width:250px;height:160px;border-radius:125px 125px 0 0;background:var(--tan)}
.price-amount{left:0;width:1200px;top:1253px;font-size:52px;font-weight:500}
.price-amount small{font-size:24px;font-weight:400}
.price-note{left:0;width:1200px;top:1326px;font-size:23px;line-height:1.4}
.email-field{left:422px;top:1406px;width:356px;height:42px;background:var(--white);display:flex}
.email-field span{flex:1;padding:13px 12px;font-size:14px;color:#777}
.email-field b{width:44px;background:var(--brown);display:flex;align-items:center;justify-content:center}

/* hooks */
.hooks{position:absolute;left:0;top:1548px;width:1200px;height:1374px;background:var(--paper)}
.section-title{left:0;width:1200px;font-size:36px;letter-spacing:2px}
.hook{position:absolute;width:330px;text-align:center}
.hook i{display:block;width:290px;height:290px;border-radius:50%;margin:0 auto 16px}
.hook span{font-size:23px;font-weight:700;font-style:italic}

/* mixes */
.mixes{position:absolute;left:0;top:2922px;width:1200px;height:480px;background:var(--clay)}
.jar{position:absolute;width:150px;height:205px;border-radius:14px 14px 6px 6px}

/* reviews */
.reviews{position:absolute;left:0;top:3402px;width:1200px;height:462px;background:var(--paper)}
.review{position:absolute;width:310px;text-align:center}
.avatar{width:68px;height:68px;border-radius:50%;margin:0 auto 8px;background:linear-gradient(#9fb7c9,#5c7d94)}
.review h4{font-size:14px;font-weight:700}
.stars{color:var(--star);font-size:12px;letter-spacing:1px;margin:2px 0 8px}
.review p{font-size:13.5px;font-style:italic;line-height:25px}

/* newsletter */
.newsletter{position:absolute;left:0;top:3864px;width:1200px;height:268px;background:var(--brown);color:var(--white)}
.subscribe{left:350px;top:151px;width:500px;height:44px;display:flex;border:1px solid var(--white)}
.subscribe span{flex:1;background:var(--white);color:#888;font-size:13px;padding:14px 12px}
.subscribe b{width:124px;display:flex;align-items:center;justify-content:center;font-size:16px;font-weight:500}

/* footer */
.footer{position:absolute;left:0;top:4132px;width:1200px;height:400px;background:var(--footer);color:var(--white)}
.col{position:absolute;top:72px}
.col h5{font-size:17px;font-weight:500;margin-bottom:14px}
.col li{list-style:none;font-size:13px;line-height:29px}
.col p{font-size:13px;line-height:24px}
.contact{display:flex;align-items:center;gap:8px;font-size:13px;line-height:29px}
.social{display:flex;gap:10px;justify-content:center}
.social span{width:40px;height:40px;border:1px solid var(--white);border-radius:50%;display:flex;align-items:center;justify-content:center;font-size:7px}
.pay{right:100px;top:352px;display:flex;gap:18px;font-size:13px;font-weight:700;color:var(--muted)}
</style>
</head>
<body>

<section class="hero">
  <div class="abs brand-top">Almond Steward</div>
  <nav class="abs nav"><span>BLOG</span><span>|</span><span>HELP</span></nav>
  <h1 class="abs display hero-title center">NATURAL PEANUT BUTTER</h1>
  <div class="abs hero-sub center">Mixed Perfectly</div>
  <div class="btn" style="left:517px;top:225px;width:166px;height:46px">Shop Now
    <svg viewBox="0 0 16 16"><circle cx="8" cy="8" r="8" fill="#fff"/><path d="M6 4l4 4-4 4" stroke="#8c5a4e" stroke-width="2" fill="none"/></svg></div>

  <svg class="abs" style="left:62px;top:340px" width="20" height="32" viewBox="0 0 20 32"><path d="M16 2L4 16l12 14" stroke="#333" stroke-width="2" fill="none"/></svg>
  <svg class="abs" style="left:1120px;top:340px" width="20" height="32" viewBox="0 0 20 32"><path d="M4 2l12 14L4 30" stroke="#333" stroke-width="2" fill="none"/></svg>

  <svg class="abs" style="left:0;top:0" width="1200" height="646" viewBox="0 0 1200 646">
    <g stroke="#9a8f82" stroke-width="1" stroke-dasharray="3 3" fill="none">
      <line x1="278" y1="385" x2="400" y2="385"/>
      <line x1="770" y1="330" x2="912" y2="330"/>
      <line x1="800" y1="470" x2="928" y2="470"/>
    </g>
    <circle cx="233" cy="385" r="42" fill="none" stroke="#f5b321" stroke-width="8" stroke-dasharray="14 6"/>
    <path d="M215 378a20 20 0 0 1 34-6M251 392a20 20 0 0 1-34 6" stroke="#f5b321" stroke-width="4" fill="none"/>
  </svg>
  <div class="abs" role="img" aria-label="Annoyed face emoji" style="left:916px;top:278px;width:84px;height:84px;border-radius:50%;background:radial-gradient(circle at 40% 35%,#ff8a3d,#e0341f)"></div>
  <div class="abs" role="img" aria-label="Smiling face emoji" style="left:933px;top:442px;width:84px;height:84px;border-radius:50%;background:radial-gradient(circle at 40% 35%,#ffe266,#f5b000)"></div>

  <div class="abs feature-label" style="left:132px;top:437px">Hassle Free Mix-in</div>
  <div class="abs feature-label" style="left:872px;top:374px">Mixed Perfectly</div>
  <div class="abs feature-label" style="left:898px;top:532px">Better Tasting</div>
</section>
<div class="abs bowl" role="img" aria-label="Bowl of swirled natural peanut butter seen from above"></div>

<section class="how">
  <div class="abs how-photo" role="img" aria-label="Little girl in glasses eating peanut butter from a jar beside a spiral mixing hook"></div>
  <h2 class="abs display how-title">HOW IT WORKS</h2>
  <div class="step" style="left:500px;top:188px">
    <svg viewBox="0 0 52 56" fill="none" stroke="#fff" stroke-width="2"><rect x="4" y="6" width="40" height="14" rx="4"/><path d="M14 20v10M24 20v10M14 30h10M8 50h36M18 30v20"/></svg>
    Use your own hand mixer or drill</div>
  <div class="step" style="left:804px;top:188px">
    <svg viewBox="0 0 52 56" fill="none" stroke="#fff" stroke-width="2"><rect x="8" y="4" width="30" height="8" rx="2"/><rect x="6" y="12" width="34" height="40" rx="5"/><circle cx="23" cy="32" r="7"/><path d="M19 32h8"/></svg>
    Mix it right in your store-bought jar</div>
  <div class="step" style="left:500px;top:331px">
    <svg viewBox="0 0 52 56" fill="none" stroke="#fff" stroke-width="2"><path d="M18 2v12M22 2v12"/><path d="M20 14c10 4-10 8 0 12s-10 8 0 12-10 8 0 12"/></svg>
    Thin-2 mm Stainless Steel hook mixes without displacing oil</div>
  <div class="step" style="left:804px;top:331px">
    <svg viewBox="0 0 52 56" fill="none" stroke="#fff" stroke-width="2"><path d="M24 4v40M16 36l8 10 8-10"/><path d="M24 12c10 4-10 8 0 12s-10 8 0 12"/></svg>
    Arrow Tip breaks up settled nuts creating top to bottom flow</div>
</section>

<section class="price">
  <div class="abs" role="img" aria-label="Jar of unmixed natural peanut butter with lid" style="left:85px;top:85px;width:252px;height:290px;border-radius:40px 40px 0 0;background:linear-gradient(#3f5e55 0 16%,#6d5a4a 17%,#4a3a2e 100%)"></div>
  <div class="abs" role="img" aria-label="Spiral hook lifting peanut butter out of an open jar" style="left:860px;top:0;width:240px;height:375px;background:linear-gradient(#d9c0a5 0 35%,#6b4b36 36%,#3e2d22 100%);border-radius:60px 60px 0 0"></div>
</section>
<div class="abs bump"></div>
<div class="btn" style="left:526px;top:1155px;width:148px;height:38px;font-size:15px">Shop Now
  <svg viewBox="0 0 16 16"><circle cx="8" cy="8" r="8" fill="#fff"/><path d="M6 4l4 4-4 4" stroke="#8c5a4e" stroke-width="2" fill="none"/></svg></div>
<div class="abs price-amount center">$ 19.99 <small>USD</small></div>
<div class="abs price-note center">Sign up for Free shipping Coupon<br>(Valid in USA and Canada only)</div>
<div class="abs email-field"><span>Email Address</span><b><svg width="16" height="16" viewBox="0 0 16 16"><path d="M1 8l14-7-5 14-2-6z" fill="#fff"/></svg></b></div>

<section class="hooks">
  <h2 class="abs display section-title center" style="top:82px">CHOOSE YOUR HOOK HOW</h2>
  <div class="hook" style="left:96px;top:175px"><i role="img" aria-label="Peanut butter and jam sandwich" style="background:radial-gradient(circle at 45% 40%,#e9c08a,#c9763a 35%,#b03a2e 60%,#7a3a24)"></i><span>Gray and Fenwick</span></div>
  <div class="hook" style="left:435px;top:175px"><i role="img" aria-label="Peanut butter spread on toast with peanuts" style="background:radial-gradient(circle at 55% 45%,#e0a860,#b8783c 45%,#4a3a30 80%,#2c2f36)"></i><span>Vellomix</span></div>
  <div class="hook" style="left:773px;top:175px"><i role="img" aria-label="Nut clusters on a white plate" style="background:radial-gradient(circle at 45% 50%,#ece8dc,#c9c2a8 30%,#8a5a2c 65%,#4a3424)"></i><span>Corwin Harbor</span></div>
  <div class="hook" style="left:96px;top:561px"><i role="img" aria-label="Apple slices with peanut butter" style="background:radial-gradient(circle at 50% 45%,#f6ece0,#e6b07a 30%,#c9302c 62%,#9a2a22)"></i><span>StoveMate</span></div>
  <div class="hook" style="left:435px;top:561px"><i role="img" aria-label="Oatmeal topped with banana and peanut butter" style="background:radial-gradient(circle at 50% 40%,#d9a45a,#e8d6b0 40%,#d2c09a 75%,#b8a27e)"></i><span>Universal Drill ¼" HEX drill bit</span></div>
  <div class="hook" style="left:773px;top:561px"><i role="img" aria-label="Peanut butter cups with a spoon" style="background:radial-gradient(circle at 45% 60%,#e08a30,#c97a3a 30%,#c9a88a 60%,#8a6a52)"></i><span>Brelda</span></div>
  <div class="hook" style="left:96px;top:947px"><i role="img" aria-label="Peanut butter smoothie cups" style="background:radial-gradient(circle at 45% 40%,#d9b890,#8a6a4e 45%,#4a3a30 80%,#2e2a28)"></i><span>Halvern Trope</span></div>
  <div class="hook" style="left:435px;top:947px"><i role="img" aria-label="Chocolate peanut butter cups" style="background:radial-gradient(circle at 50% 60%,#e89a44,#b0643a 40%,#6b3a24 70%,#e8ddd0)"></i><span>Glowline Modern</span></div>
  <div class="hook" style="left:773px;top:947px"><i role="img" aria-label="Peanut butter energy balls in a jar" style="background:radial-gradient(circle at 45% 45%,#c08a50,#8a5a34 45%,#5a4434 75%,#3a3a3a)"></i><span>Glowline Retro</span></div>
</section>

<section class="mixes">
  <h2 class="abs display center" style="left:0;width:1200px;top:60px;font-size:40px;line-height:56px;color:var(--white)">Mixes in All Natural Nut Butters<br>Right in their own jars.</h2>
  <div class="btn" style="left:518px;top:186px;width:150px;height:40px;font-size:15px">All Of Them
    <svg viewBox="0 0 16 16"><circle cx="8" cy="8" r="8" fill="#fff"/><path d="M6 4l4 4-4 4" stroke="#8c5a4e" stroke-width="2" fill="none"/></svg></div>
  <div class="jar" role="img" aria-label="Jar of almond butter with almonds" style="left:77px;top:275px;background:linear-gradient(#4a3a34 0 16%,#e07a48 17%,#c9603a)"></div>
  <div class="jar" role="img" aria-label="Jar of cashew butter with cashews" style="left:320px;top:275px;background:linear-gradient(#4a3a34 0 16%,#b8b85a 17%,#9a9a3a)"></div>
  <div class="jar" role="img" aria-label="Jar of hazelnut butter with hazelnuts" style="left:562px;top:275px;background:linear-gradient(#4a3a34 0 16%,#d8c050 17%,#b89a30)"></div>
  <div class="jar" role="img" aria-label="Jar of sunflower seed butter" style="left:780px;top:275px;background:linear-gradient(#4a3a34 0 16%,#c8c060 17%,#a89a3a)"></div>
  <div class="jar" role="img" aria-label="Jar of peanut butter with peanuts" style="left:1017px;top:275px;background:linear-gradient(#4a3a34 0 16%,#e88a4a 17%,#c96a3a)"></div>
</section>

<section class="reviews">
  <h2 class="abs display center" style="left:0;width:1200px;top:86px;font-size:36px">What people are saying...</h2>
  <div class="review" style="left:96px;top:186px"><div class="avatar" role="img" aria-label="Customer portrait"></div><h4>- John Doe</h4><div class="stars">★★★★★</div><p>"Sed ut perspiciatis unde omnis ie natus error sit voluptatem accusantium dolue laudantium, totam rem aperiue ipsa quae ab illo inventore veritatis et quasi architecto beatae"</p></div>
  <div class="review" style="left:445px;top:186px"><div class="avatar" role="img" aria-label="Customer portrait" style="background:linear-gradient(#f3d3b0,#c98a5a)"></div><h4>- John Doe</h4><div class="stars">★★★★★</div><p>"Sed ut perspiciatis unde omnis ie natus error sit voluptatem accusantium dolue laudantium, totam rem aperiue ipsa quae ab illo inventore veritatis et quasi architecto beatae"</p></div>
  <div class="review" style="left:793px;top:186px"><div class="avatar" role="img" aria-label="Customer portrait" style="background:linear-gradient(#e8e8e8,#a8a8a8)"></div><h4>- John Doe</h4><div class="stars">★★★★★</div><p>"Sed ut perspiciatis unde omnis ie natus error sit voluptatem accusantium dolue laudantium, totam rem aperiue ipsa quae ab illo inventore veritatis et quasi architecto beatae"</p></div>
</section>

<section class="newsletter">
  <h2 class="abs display center" style="left:0;width:1200px;top:74px;font-size:25px;letter-spacing:1px">SUBSCRIBE TO OUR NEWSLETTER</h2>
  <p class="abs center" style="left:0;width:1200px;top:113px;font-size:13px">A short sentence describing what someone will receive by subscribing</p>
  <div class="abs subscribe"><span>Enter Your Email Address</span><b>SUBSCRIBE</b></div>
</section>

<footer class="footer">
  <div class="col" style="left:103px"><h5>QUICK LINKS</h5><ul><li>Search</li><li>Become a Seller</li><li>Contact Us</li><li>Refund Policy</li><li>Shipping Policy</li><li>Privacy Policy</li><li>Terms of Service</li></ul></div>
  <div class="col" style="left:298px"><h5>MAIN MENU</h5><ul><li>&nbsp;Home</li><li>About Us</li><li>Shop</li><li>Blog</li><li>Contact &amp; FAQ</li><li>Press &amp; Awards</li></ul></div>
  <div class="col" style="left:481px;width:350px"><h5>PURCHASING &amp;DISTRIBUTION</h5>
    <p>Lorem ipsum dolor sit amet, consectetur adipiscing elit, sed do eiusmod tempor incididunt ut labore et dolore magna aliqua. Quis ipsum suspendisse ultrices</p>
    <div class="contact"><svg width="12" height="10" viewBox="0 0 12 10"><rect width="12" height="10" fill="#fff"/><path d="M0 0l6 5 6-5" stroke="#111" fill="none"/></svg>info@almondsteward.com</div>
    <div class="contact"><svg width="12" height="12" viewBox="0 0 12 12"><path d="M2 1l3 0 1 3-2 1c1 2 2 3 3 3l1-2 3 1v3c-6 0-10-4-10-9z" fill="#fff"/></svg>1-800-555-0142</div>
    <div class="contact"><svg width="10" height="13" viewBox="0 0 10 13"><path d="M5 0a5 5 0 0 1 5 5c0 3-5 8-5 8S0 8 0 5a5 5 0 0 1 5-5z" fill="#fff"/><circle cx="5" cy="5" r="2" fill="#111"/></svg>123 Avenue name, City name 10150, United States</div>
  </div>
  <div class="col" style="left:870px;width:230px;top:80px;text-align:center">
    <div style="font-size:22px;font-weight:500;letter-spacing:1px;margin-bottom:26px">Almond Steward</div>
    <div class="social"><span>Nookly</span><span>Lumo</span><span>Tweedle</span><span>Reelcast</span></div>
  </div>
  <p class="abs" style="left:120px;top:356px;font-size:12px">Copyright © 2021 Almond Steward. All Rights Reserved.</p>
  <div class="abs pay"><span>Tallypay</span><span>Circlecard</span><span>Meridian</span><span>Pocketsend</span><span>Orchard Pay</span></div>
</footer>

</body>
</html>
```